Modern, corporate management consultancy firm needs a new website

We need a website for an Australian based management consultancy firm.

The company name is Norcott Strategy Partners.

We are looking for a parallax style wordpress site.

The site needs to provide the following functions:

1) subscribe function
2) links to social media (twitter, linkedin and mail)
3) a gated document section where people can download pdf's from the site after registering or providing name, company, position, email and contact number.

Attached is the company logo, would like to see designs that incorporate the dark blue and silver in the logo and separated into the following sections (Home, About, Services (with 4 options), Our Team, Links, Contacts.

Need the site to be easy to navigate and updated.

Potentially a News Section that can be updated regularly.

Target Market(s)

Target market is SME, business owners and directors

Industry/Entity Type

Management Consulting

Coding

Coded - Design and coding required

Number of Pages Required

1 page

Font styles to use
Sans Serif

Colors
0255a3
cbcbcb
757575
000000

Requirements
Must have
• Must be easy to read and use
Nice to have
• Features are listed on initial brief

```html
<!DOCTYPE html>
<html lang="en">
<head>
<meta charset="utf-8">
<title>Norcott Strategy Partners</title>
<link href="https://fonts.googleapis.com/css2?family=Roboto:ital,wght@0,300;0,400;0,500;0,700;1,400&family=Roboto+Slab:wght@300;400&display=swap" rel="stylesheet">
<style>
:root{
  --blue:#0255a3;
  --blue-deep:#0a3f78;
  --silver:#cbcbcb;
  --grey:#757575;
  --black:#000000;
  --ink:#2b2b2b;
  --pale:#e9eef5;
  --white:#ffffff;
}
*{margin:0;padding:0;box-sizing:border-box}
html,body{width:1200px;height:3376px;overflow:hidden}
body{font-family:"Roboto",Arial,sans-serif;color:var(--ink);background:var(--white);position:relative}
section,header,footer{position:absolute;left:0;width:1200px;overflow:hidden}

/* Hero */
.hero{top:0;height:656px}
.hero-photo{position:absolute;inset:0;background:linear-gradient(180deg,#7f9fbf 0%,#5d86b3 30%,#1d5d9c 55%,#2a6aa8 75%,#3c77ad 100%)}
.hero-person{position:absolute;left:40px;top:10px;width:360px;height:646px;background:linear-gradient(180deg,#8a8f96 0%,#4a4f57 45%,#3a3e45 100%);border-radius:160px 160px 0 0;opacity:.55}
.hero-band{position:absolute;left:0;right:0;top:170px;height:420px;background:rgba(2,85,163,.55)}
.nav{position:absolute;top:0;left:0;right:0;height:34px;display:flex;justify-content:center;gap:44px;align-items:center;background:rgba(0,0,0,.18)}
.nav a{color:var(--white);font-size:15px;text-decoration:none;letter-spacing:.5px;text-transform:uppercase}
.nav a.active{color:#bcd8f5;border-bottom:2px solid #bcd8f5;padding-bottom:3px}
.brand{position:absolute;left:388px;top:260px;display:flex;align-items:center;gap:22px}
.brand-mark{width:104px;height:104px;border:2px solid var(--white);border-radius:50%}
.brand-name{color:var(--white);font-size:40px;font-weight:400;line-height:1.1}
.brand-tag{color:var(--white);font-size:13px;letter-spacing:3px;text-transform:uppercase;margin-top:8px;opacity:.85}

/* About */
.about{top:656px;height:304px;text-align:center;background:var(--white)}
.section-title{font-size:44px;font-weight:400;color:#4a4a4a;margin-top:52px}
.section-title b{color:var(--blue);font-weight:500}
.about p{width:700px;margin:26px auto 0;font-size:14px;line-height:22px;color:var(--grey)}
.btn-outline{display:inline-block;margin-top:28px;border:1.5px solid #555;padding:8px 26px;font-size:14px;color:#333;letter-spacing:1px;text-transform:uppercase}

/* Services */
.services{top:960px;height:500px;background:linear-gradient(180deg,#3a76b8 0%,var(--blue) 55%,#0b4e95 100%);text-align:center}
.services h2{color:var(--white);font-size:44px;font-weight:400;margin-top:70px}
.service-row{position:absolute;top:200px;left:80px;display:flex;gap:20px}
.service{width:252px;height:220px;border:1.5px solid rgba(255,255,255,.35);background:rgba(255,255,255,.06);color:rgba(255,255,255,.7);padding:24px 20px;font-size:17px}
.service.active{border:2px solid var(--white);background:rgba(2,60,120,.35);color:var(--white)}
.service svg{display:block;margin:0 auto 18px;width:62px;height:62px}
.service .s-title{font-size:17px;line-height:22px}
.service p{font-size:12.5px;line-height:18px;margin-top:12px;opacity:.9}

/* Subscribe */
.subscribe{top:1460px;height:268px;background:var(--pale)}
.sub-head{text-align:center;margin-top:50px;font-size:15px;color:#444}
.sub-head strong{font-size:28px;color:var(--blue);font-weight:500;margin-right:8px}
.fields{position:absolute;top:116px;left:100px;display:flex;gap:48px}
.field{display:flex;align-items:center;gap:14px}
.field svg{width:26px;height:26px}
.field span{display:block;width:440px;height:52px;background:var(--white);border:1px solid #d3d9e2;padding:16px 14px;font-size:14px;color:#777}
.btn-sub{position:absolute;left:446px;top:246px;width:308px;height:48px;background:var(--blue);color:var(--white);font-size:17px;text-align:center;line-height:48px;z-index:3}

/* Statement */
.statement{top:1728px;height:532px}
.statement-photo{position:absolute;inset:0;background:linear-gradient(120deg,#6c6e72 0%,#b8b6b2 40%,#8d8f93 65%,#4e5258 100%)}
.statement-shade{position:absolute;inset:0;background:rgba(20,20,25,.42)}
.statement blockquote{position:absolute;left:210px;top:190px;width:800px;color:var(--white);font-family:"Roboto Slab",Georgia,serif;font-size:38px;font-weight:300;line-height:48px;text-align:center}
.statement em{font-style:italic}

/* News */
.news{top:2260px;height:600px;background:var(--white);text-align:center}
.news .section-title{margin-top:56px}
.news-row{position:absolute;top:128px;left:80px;display:flex;gap:24px;text-align:left}
.post{width:328px}
.post-photo{height:212px;background:linear-gradient(135deg,#b9c4d0,#6f87a2)}
.post:nth-child(2) .post-photo{background:linear-gradient(135deg,#d9dde2,#6c7c90)}
.post:nth-child(3) .post-photo{background:linear-gradient(135deg,#e0a64b,#7e8a96)}
.post h3{font-size:16px;font-weight:700;color:#222;margin-top:10px}
.post time{display:block;font-size:11px;color:#999;margin-top:3px}
.post p{font-size:13px;line-height:18px;color:var(--grey);margin-top:8px}
.btn-dark{position:absolute;left:530px;top:506px;width:140px;height:40px;background:var(--black);color:var(--white);line-height:40px;font-size:13px;letter-spacing:1px}

/* Footer */
.footer{top:2860px;height:516px}
.footer-photo{position:absolute;inset:0;background:linear-gradient(180deg,#0c1a33 0%,#1c3b6b 45%,#2f4d73 60%,#0d1526 100%)}
.contact-card{position:absolute;left:452px;top:40px;width:296px;height:380px;background:rgba(255,255,255,.14);text-align:center;color:var(--white)}
.phone-badge{width:72px;height:72px;border-radius:50%;background:var(--white);margin:24px auto 0;display:flex;align-items:center;justify-content:center}
.phone-num{font-size:30px;margin-top:22px}
.address{font-size:15px;line-height:24px;margin-top:18px}
.email{font-size:15px;margin-top:14px}
.socials{display:flex;justify-content:center;gap:12px;margin-top:26px}
.socials span{width:34px;height:34px;border-radius:50%;background:var(--blue);display:flex;align-items:center;justify-content:center}
.socials span.mail{background:#ffffff30;border:1.5px solid var(--white)}
.up{position:absolute;left:584px;top:452px;width:32px;height:32px;border-radius:50%;background:rgba(255,255,255,.25)}
.copyright{position:absolute;bottom:16px;left:0;right:0;text-align:center;color:#cbcbcb;font-size:12px}
</style>
</head>
<body>

<header class="hero">
  <div class="hero-photo" role="img" aria-label="Harbour city skyline with marina under a blue sky"></div>
  <div class="hero-band"></div>
  <div class="hero-person" role="img" aria-label="Consultant in a grey suit standing with arms folded"></div>
  <nav class="nav">
    <a class="active" href="#">Home</a><a href="#">About</a><a href="#">Services</a><a href="#">Our Team</a><a href="#">Links</a><a href="#">Contacts</a>
  </nav>
  <div class="brand">
    <div class="brand-mark"></div>
    <div>
      <div class="brand-name">Norcott Strategy Partners</div>
      <div class="brand-tag">Business Performance Improvement</div>
    </div>
  </div>
</header>

<section class="about">
  <h2 class="section-title">About <b>Norcott STRATEGY PARTNERS</b></h2>
  <p>Norcott Strategy Partners is a boutique management consulting firm that serves micro, small and mid-size ASX-listed and private companies.<br>We are a team of specialist consultants and performance improvement, process optimisation, profit maximisation and negotiation/mediation.</p>
  <span class="btn-outline">Read More</span>
</section>

<section class="services">
  <h2>Services We Provide</h2>
  <div class="service-row">
    <div class="service active">
      <svg viewBox="0 0 62 62" fill="none" stroke="#fff" stroke-width="2.5"><rect x="14" y="10" width="34" height="44" rx="3"/><rect x="23" y="6" width="16" height="8" rx="2"/><path d="M21 32l7 7 13-14"/></svg>
      <div class="s-title">Business Health Checks</div>
      <p>Norcott Strategy Partners provides a fixed fee health check for your business. We will meet with you and your key personnel.</p>
    </div>
    <div class="service">
      <svg viewBox="0 0 62 62" fill="none" stroke="#fff" stroke-width="2.5" opacity=".75"><path d="M8 50h46"/><path d="M12 42l14-14 9 9 17-19"/><path d="M42 18h10v10"/></svg>
      <div class="s-title">Business Performance Consulting</div>
    </div>
    <div class="service">
      <svg viewBox="0 0 62 62" fill="none" stroke="#fff" stroke-width="2.5" opacity=".75"><circle cx="31" cy="31" r="20"/><path d="M31 19v12l9 6"/></svg>
      <div class="s-title">Turnaround Management</div>
    </div>
    <div class="service">
      <svg viewBox="0 0 62 62" fill="none" stroke="#fff" stroke-width="2.5" opacity=".75"><circle cx="31" cy="31" r="20"/><circle cx="31" cy="31" r="9"/><path d="M24 24l-8-8M38 24l8-8M24 38l-8 8M38 38l8 8"/></svg>
      <div class="s-title">Independent Insolvency Advice</div>
    </div>
  </div>
</section>

<section class="subscribe">
  <div class="sub-head"><strong>Stay Conected!</strong>Sign up for our newsletter and get first pick off discounts and more!</div>
  <div class="fields">
    <div class="field">
      <svg viewBox="0 0 26 26" fill="#333"><circle cx="13" cy="8" r="5"/><path d="M3 24c0-6 4-9 10-9s10 3 10 9z"/></svg>
      <span>Name</span>
    </div>
    <div class="field">
      <svg viewBox="0 0 26 26" fill="#333"><rect x="2" y="6" width="22" height="15" rx="1"/><path d="M3 7l10 8 10-8" stroke="#fff" stroke-width="1.6" fill="none"/></svg>
      <span>Email Address</span>
    </div>
  </div>
</section>
<div class="btn-sub" style="top:1706px">Subscribe Newsletter</div>

<section class="statement">
  <div class="statement-photo" role="img" aria-label="Business team meeting around a table"></div>
  <div class="statement-shade"></div>
  <blockquote>Providing tailored Specialist ADVICE to businesses, working together to identity <em>problem areas, resolve issues and improve performance.</em></blockquote>
</section>

<section class="news">
  <h2 class="section-title">Latest <b>News Post</b></h2>
  <div class="news-row">
    <article class="post">
      <div class="post-photo" role="img" aria-label="Business partners shaking hands in an office"></div>
      <h3>Lorem ipsum is a dummy</h3>
      <time>September 08, 2015</time>
      <p>Lorem Ipsum is simply dummy text of the printing and typesetting industry. Lorem Ipsum has been the industry's standard dummy text ever since...</p>
    </article>
    <article class="post">
      <div class="post-photo" role="img" aria-label="Colleagues reviewing charts on a laptop"></div>
      <h3>Lorem ipsum is a dummy</h3>
      <time>September 08, 2015</time>
      <p>Lorem Ipsum is simply dummy text of the printing and typesetting industry. Lorem Ipsum has been the industry's standard dummy text ever since...</p>
    </article>
    <article class="post">
      <div class="post-photo" role="img" aria-label="Engineers in hard hats on a building site"></div>
      <h3>Lorem ipsum is a dummy</h3>
      <time>September 08, 2015</time>
      <p>Lorem Ipsum is simply dummy text of the printing and typesetting industry. Lorem Ipsum has been the industry's standard dummy text ever since...</p>
    </article>
  </div>
  <div class="btn-dark">READ MORE</div>
</section>

<footer class="footer">
  <div class="footer-photo" role="img" aria-label="Coastal highway at night with light trails"></div>
  <div class="contact-card">
    <div class="phone-badge">
      <svg width="34" height="34" viewBox="0 0 24 24" fill="none" stroke="#0255a3" stroke-width="1.8"><path d="M6.6 3.5l3 3.2-1.8 2.4a13 13 0 0 0 7.1 7.1l2.4-1.8 3.2 3-1.7 3A17 17 0 0 1 3.5 5.2z"/></svg>
    </div>
    <div class="phone-num">+61 2 9000 4821</div>
    <div class="address">Level 10, 52 Harbour Lane<br>Sydney NSW 2000 Australia</div>
    <div class="email">info@norcottstrategy.com.au</div>
    <div class="socials">
      <span></span><span></span><span></span>
      <span class="mail"><svg width="16" height="12" viewBox="0 0 16 12" fill="none" stroke="#fff" stroke-width="1.4"><rect x="1" y="1" width="14" height="10"/><path d="M1 1l7 6 7-6"/></svg></span>
    </div>
  </div>
  <div class="up"></div>
  <div class="copyright">© Norcott Strategy Partners - 2015. All rights reserved.</div>
</footer>

</body>
</html>
```